Design Card that Captures Life's Moments

Thinking black and white design with maybe some accent colors. Open to others too. Looking for bold and modern to accompany new logo design. For the side without my info, would have tagline of "Capturing Life's Moments" with either logo or website petravossimaging.com. I want the tagline to dominate and be the main focus of that side.

Target Market(s)

Something that can appeal to people who might be interested in family/kids, business, sports, commercial, or birth/newborn photography.

Industry/Entity Type

Professional Photography

Contact Information for Business Card

Font styles to use
Sans Serif
Script
Other font styles liked:
• Go with Logo, but the tagline could be script that popped.

Requirements
Must have
• See details above! Wow factor! Make someone pick my card up and take it home or at least to look at it further.
• Tagline: Capturing Life's Moments (Main text on side without name)
• INFO:
• Petra Voss-Hale - Photographer
• 555-318-0462 - Cell and for SMS
• www.petravossimaging.com - Website (maybe on side with tagline?)
• petra@petrastudioframes.com - Email
Nice to have
• JUST AN IDEA... I would like to see Capturing Life's Moment really take over most of one side of the card. Think greeting card. Where you can't miss it. It is in your face, but nice and elegant. Maybe cursive, but could work with other font. Instead of logo on tagline side, just have petravossimaging.com in smaller text along one of the edges.
Should not have
• Too simple I could of created it, like with only my logo and some typed text.

```html
<!DOCTYPE html>
<html lang="en">
<head>
<meta charset="utf-8">
<title>Petra Voss Imaging – Business Card</title>
<link rel="stylesheet" href="https://fonts.googleapis.com/css2?family=Courier+Prime&family=Open+Sans:wght@400&family=Questrial&display=swap">
<style>
  :root {
    --card-highlight: #727272;
    --card-light: #5c5c5c;
    --card-mid: #444444;
    --card-dark: #262626;
    --card-deep: #1e1e1e;
    --ink: #ffffff;
    --ink-soft: rgba(255, 255, 255, 0.92);
  }
  html, body {
    margin: 0;
    padding: 0;
    width: 1200px;
    height: 720px;
    overflow: hidden;
    background: var(--card-deep);
  }
  .business-card {
    position: relative;
    width: 1200px;
    height: 720px;
    overflow: hidden;
    background:
      radial-gradient(ellipse 520px 420px at 400px 280px, var(--card-highlight) 0%, rgba(114,114,114,0) 100%),
      linear-gradient(160deg, var(--card-light) 0%, var(--card-mid) 55%, var(--card-dark) 100%);
    color: var(--ink);
  }
  .card-backdrop {
    position: absolute;
    inset: 0;
    width: 1200px;
    height: 720px;
  }
  .brand-name {
    position: absolute;
    left: 88px;
    top: 112px;
    margin: 0;
    font-family: "Questrial", sans-serif;
    font-weight: 400;
    font-size: 64px;
    line-height: 1;
    letter-spacing: 1px;
    color: var(--ink);
  }
  .person-name {
    position: absolute;
    left: 128px;
    top: 328px;
    margin: 0;
    font-family: "Courier Prime", "Courier New", monospace;
    font-weight: 400;
    font-size: 64px;
    line-height: 1;
    color: var(--ink);
  }
  .person-role {
    position: absolute;
    left: 244px;
    top: 406px;
    margin: 0;
    font-family: "Open Sans", sans-serif;
    font-weight: 400;
    font-size: 30px;
    line-height: 1;
    letter-spacing: 2.5px;
    color: var(--ink-soft);
  }
  .contact-list {
    position: absolute;
    right: 91px;
    top: 560px;
    margin: 0;
    padding: 0;
    list-style: none;
    text-align: right;
    font-family: "Questrial", sans-serif;
    color: var(--ink);
  }
  .contact-phone {
    font-size: 40px;
    line-height: 48px;
    letter-spacing: 0.5px;
  }
  .contact-email {
    font-size: 33px;
    line-height: 44px;
  }
</style>
</head>
<body>
  <main class="business-card">
    <svg class="card-backdrop" viewBox="0 0 1200 720" aria-hidden="true">
      <defs>
        <linearGradient id="shadow-sweep" x1="0" y1="0" x2="1" y2="0">
          <stop offset="0" stop-color="#303030"/>
          <stop offset="0.6" stop-color="#262626"/>
          <stop offset="1" stop-color="#1e1e1e"/>
        </linearGradient>
        <linearGradient id="wave-glow" x1="0" y1="1" x2="1" y2="0">
          <stop offset="0" stop-color="#ffffff" stop-opacity="0"/>
          <stop offset="0.45" stop-color="#ffffff" stop-opacity="0.22"/>
          <stop offset="1" stop-color="#ffffff" stop-opacity="0.05"/>
        </linearGradient>
        <radialGradient id="aperture-tone" cx="0.5" cy="0.5" r="0.5">
          <stop offset="0" stop-color="#2a2a2a"/>
          <stop offset="0.7" stop-color="#3a3a3a"/>
          <stop offset="1" stop-color="#4a4a4a" stop-opacity="0.6"/>
        </radialGradient>
      </defs>
      <path class="shadow-sweep" d="M560 720 C620 520 760 390 900 300 C1010 230 1110 120 1200 60 L1200 720 Z" fill="url(#shadow-sweep)"/>
      <path class="wave-line" d="M420 470 C560 360 700 300 820 250 C960 190 1080 110 1200 50" fill="none" stroke="url(#wave-glow)" stroke-width="2"/>
      <path class="wave-line" d="M440 500 C600 410 720 330 860 270 C990 210 1100 140 1200 90" fill="none" stroke="url(#wave-glow)" stroke-width="1" opacity="0.5"/>
      <circle class="aperture-mark" cx="1174" cy="628" r="140" fill="url(#aperture-tone)" role="img" aria-label="Faint camera aperture decoration"/>
    </svg>

    <p class="brand-name">Petra Voss Imaging</p>

    <h1 class="person-name">Petra Voss-Hale</h1>
    <p class="person-role">PHOTOGRAPHER</p>

    <ul class="contact-list">
      <li class="contact-phone">555-318-0462</li>
      <li class="contact-email">petra@petrastudioframes.com</li>
    </ul>
  </main>
</body>
</html>
```